law firm website

We need a website for our law firm that is based in Kabul, Afghanistan. We provide legal and government affairs services for the international community. We would like to see designs that use the colors of our logo, designs that are elegant and simple, yet not boring or over the top. No law or law related symbols or pictures. We would like clocks that show times for Kabul, Dubai and Washington DC.
Updates
Reason: No designs that are up to the task as yet. Perhaps we should stop using picture of people, that obviously don't work with us, in the website. If you are to use pictures, please try using pictures of Afghanistan mountains, art, craft etc. Also, please make the clocks very small - they seem to be dominating the website. We do not sell clocks or watches - we are a law firm. Hope you all understand and thank you for your designs to date.
Deal All,
Industry/Entity Type
Government
Requirements
Must have
- our logo.
the following phrases/words in flash.
"international standards" "local expertise" "integrity" "clarity" "commitment" "Afghanistan"
clocks: kabul, dubai, washington dc
Should not have
- law related pictures
afghanistan flag colors

```html
<!DOCTYPE html>
<html lang="en">
<head>
<meta charset="utf-8">
<title>Kabul Counsel Partners — Services</title>
<link rel="stylesheet" href="https://fonts.googleapis.com/css2?family=Noto+Sans:wght@400;700&family=PT+Sans:wght@400;700&display=swap">
<style>
  :root {
    --brand-blue: #4a8cc8;
    --text-grey: #9a9a9a;
    --heading-grey: #7d7d7d;
    --nav-grey: #a3a3a3;
    --rule-grey: #cfcfcf;
    --divider: #bdbdbd;
    --page-bg: #ffffff;
    --frame: #e3e3e3;
  }
  * { margin: 0; padding: 0; box-sizing: border-box; }
  html, body { width: 1200px; height: 928px; overflow: hidden; background: var(--page-bg); }
  body { font-family: "Noto Sans", sans-serif; position: relative; }

  .page {
    position: absolute; left: 7px; top: 0; width: 1186px; height: 928px;
    border-left: 1px solid var(--frame); border-right: 1px solid var(--frame);
  }

  .sidebar {
    position: absolute; left: 0; top: 0; width: 341px; height: 928px;
    border-right: 2px solid var(--divider);
  }
  .sidebar::before { content: ""; position: absolute; right: -2px; top: 0; width: 2px; height: 50px; background: var(--page-bg); }

  .brand { position: absolute; left: 30px; top: 14px; display: flex; align-items: flex-start; gap: 14px; }
  .brand-mark { width: 44px; height: 44px; border-radius: 50%; background: var(--brand-blue); flex: none; }
  .brand-name { font-family: "PT Sans", sans-serif; font-size: 22px; line-height: 26px; color: var(--brand-blue); }

  .main-nav { position: absolute; left: 16px; top: 98px; width: 308px; list-style: none; }
  .main-nav li {
    height: 48.6px; border-bottom: 1px solid var(--rule-grey);
    display: flex; align-items: center; padding-left: 6px;
    font-family: "PT Sans", sans-serif; font-size: 24px; letter-spacing: 1px; color: var(--nav-grey);
  }
  .main-nav li svg { margin-right: 16px; }

  .world-clocks {
    position: absolute; left: 22px; top: 520px; width: 300px;
    display: flex; justify-content: space-between; list-style: none;
  }
  .world-clocks li {
    width: 96px; display: flex; flex-direction: column; align-items: center;
    font-family: "PT Sans", sans-serif; font-size: 11px; letter-spacing: 1px; color: var(--nav-grey);
  }
  .world-clocks svg { margin-bottom: 5px; }

  .content { position: absolute; left: 369px; top: 0; width: 797px; }
  .slogan {
    margin-top: 8px; height: 40px; font-family: "PT Sans", sans-serif;
    font-size: 26px; letter-spacing: 4px; color: var(--brand-blue);
  }
  .slogan span { color: var(--nav-grey); }

  .hero {
    position: relative; height: 220px; margin-top: 2px;
    background: linear-gradient(90deg, #2f3a46 0%, #4f7fa8 14%, #7fb6e0 38%, #8cc3ea 60%, #d9bf9a 80%, #c9a478 100%);
  }
  .hero-title {
    position: absolute; left: 136px; top: 95px;
    font-family: "PT Sans", sans-serif; font-weight: 700; font-size: 30px; letter-spacing: 3px; color: #ffffff;
  }
  .hero-rule { height: 3px; background: var(--brand-blue); margin-top: 6px; }

  .section-title {
    margin-top: 24px; font-family: "Noto Sans", sans-serif; font-weight: 400; font-size: 19px; color: var(--brand-blue);
  }

  .service { margin-top: 18px; overflow: hidden; }
  .service-photo { float: left; width: 74px; height: 108px; margin: 0 14px 0 0; }
  .photo-corporate { background: linear-gradient(160deg, #4a4040 0%, #8a6a5c 45%, #6e1e22 100%); }
  .photo-tax { background: linear-gradient(160deg, #8a6e4e 0%, #c7a98a 50%, #3c4350 100%); }

  .service-title {
    font-family: "Noto Sans", sans-serif; font-weight: 700; font-size: 17px; color: var(--heading-grey);
    line-height: 20px; display: flex; align-items: center;
  }
  .service-title svg { margin-right: 10px; }
  .service p, .service ul {
    font-size: 16px; line-height: 19.3px; letter-spacing: 0.2px; color: var(--text-grey); text-align: justify;
  }
  .service p + p { margin-top: 19px; }
  .service ul { list-style: none; text-align: left; }
  .service li { display: flex; align-items: center; }
  .service li::before { content: ""; width: 7px; height: 7px; background: var(--rule-grey); margin-right: 4px; flex: none; }
  .service-tax { margin-top: 22px; }
</style>
</head>
<body>
<div class="page">
  <aside class="sidebar">
    <div class="brand">
      <span class="brand-mark"></span>
      <span class="brand-name">Kabul Counsel<br>Partners</span>
    </div>
    <ul class="main-nav">
      <li><svg width="11" height="14" viewBox="0 0 11 14"><path d="M0 0L11 7L0 14Z" fill="#b9b9b9"/></svg>HOME</li>
      <li><svg width="11" height="14" viewBox="0 0 11 14"><path d="M0 0L11 7L0 14Z" fill="#b9b9b9"/></svg>ABOUT US</li>
      <li><svg width="11" height="14" viewBox="0 0 11 14"><path d="M0 0L11 7L0 14Z" fill="#b9b9b9"/></svg>PEOPLE</li>
      <li><svg width="11" height="14" viewBox="0 0 11 14"><path d="M0 0L11 7L0 14Z" fill="#b9b9b9"/></svg>SERVICES</li>
      <li><svg width="11" height="14" viewBox="0 0 11 14"><path d="M0 0L11 7L0 14Z" fill="#b9b9b9"/></svg>ETHICS</li>
      <li><svg width="11" height="14" viewBox="0 0 11 14"><path d="M0 0L11 7L0 14Z" fill="#b9b9b9"/></svg>PUBLICATIONS</li>
      <li><svg width="11" height="14" viewBox="0 0 11 14"><path d="M0 0L11 7L0 14Z" fill="#b9b9b9"/></svg>LEXBRIDGE</li>
      <li><svg width="11" height="14" viewBox="0 0 11 14"><path d="M0 0L11 7L0 14Z" fill="#b9b9b9"/></svg>CONTACT US</li>
    </ul>

    <ul class="world-clocks">
      <li>
        <svg width="34" height="34" viewBox="0 0 34 34">
          <circle cx="17" cy="17" r="15.5" fill="none" stroke="#4a8cc8" stroke-width="1.5"/>
          <line x1="17" y1="17" x2="17" y2="9" stroke="#7d7d7d" stroke-width="2" stroke-linecap="round" transform="rotate(315 17 17)"/>
          <line x1="17" y1="17" x2="17" y2="5" stroke="#7d7d7d" stroke-width="1.2" stroke-linecap="round" transform="rotate(180 17 17)"/>
          <circle cx="17" cy="17" r="1.5" fill="#4a8cc8"/>
        </svg>KABUL
      </li>
      <li>
        <svg width="34" height="34" viewBox="0 0 34 34">
          <circle cx="17" cy="17" r="15.5" fill="none" stroke="#4a8cc8" stroke-width="1.5"/>
          <line x1="17" y1="17" x2="17" y2="9" stroke="#7d7d7d" stroke-width="2" stroke-linecap="round" transform="rotate(300 17 17)"/>
          <line x1="17" y1="17" x2="17" y2="5" stroke="#7d7d7d" stroke-width="1.2" stroke-linecap="round"/>
          <circle cx="17" cy="17" r="1.5" fill="#4a8cc8"/>
        </svg>DUBAI
      </li>
      <li>
        <svg width="34" height="34" viewBox="0 0 34 34">
          <circle cx="17" cy="17" r="15.5" fill="none" stroke="#4a8cc8" stroke-width="1.5"/>
          <line x1="17" y1="17" x2="17" y2="9" stroke="#7d7d7d" stroke-width="2" stroke-linecap="round" transform="rotate(30 17 17)"/>
          <line x1="17" y1="17" x2="17" y2="5" stroke="#7d7d7d" stroke-width="1.2" stroke-linecap="round"/>
          <circle cx="17" cy="17" r="1.5" fill="#4a8cc8"/>
        </svg>WASHINGTON DC
      </li>
    </ul>
  </aside>

  <main class="content">
    <div class="slogan">MY WEBSITE <span>SLOGAN</span></div>
    <div class="hero" role="img" aria-label="Banner photograph: dark and light chess pieces on a blue background">
      <div class="hero-title">LOCAL EXPERTISE</div>
    </div>
    <div class="hero-rule"></div>

    <h2 class="section-title">ALL OUR SERVICES</h2>

    <section class="service">
      <div class="service-photo photo-corporate" role="img" aria-label="Photograph of a businesswoman on the phone"></div>
      <h3 class="service-title"><svg width="7" height="11" viewBox="0 0 7 11"><path d="M0 0L7 5.5L0 11Z" fill="#8a8a8a"/></svg>Corporate and Investment</h3>
      <p>Specific and integrated full legal services to organizations doing business, and overseas investors looking to do business, in Afghanistan. We provide a wide range of specific and integrated legal services to organizations doing business, and overseas investors looking to do business, in Afghanistan. We have the knowledge and experience to provide legal advice, along with the cultural and business support, necessary for clients to successfully establish and maintain their presence in Afghanistan. We provide our international client base with a full range of legal services, and work in conjunction with our clients' other advisers to ensure that all of their needs are met. Part of our corporate offering consists of legal advice regarding the formation of companies, establishment of branch and representative offices, and related agency arrangements, both inside and outside Afghanistan.</p>
      <p>We offer a comprehensive, entry to exit service that includes advising on:</p>
      <ul>
        <li>inward investment projects including licensing and incorporation in Afghanistan</li>
        <li>mergers, acquisitions and disposals</li>
        <li>corporate structuring and restructuring</li>
        <li>changes to ownership and management structures</li>
        <li>corporate governance and duties of directors</li>
        <li>Afghan corporate laws and regulations</li>
        <li>regulatory strategies and compliance</li>
        <li>establishment of branch and representative offices of foreign companies</li>
        <li>commercial agencies, sponsorship and related arrangements</li>
        <li>shareholder and joint venture agreements</li>
        <li>investment laws</li>
        <li>shareholder and management disputes</li>
      </ul>
    </section>

    <section class="service service-tax">
      <div class="service-photo photo-tax" role="img" aria-label="Photograph of a businesswoman"></div>
      <h3 class="service-title"><svg width="7" height="11" viewBox="0 0 7 11"><path d="M0 0L7 5.5L0 11Z" fill="#8a8a8a"/></svg>Tax</h3>
      <p>The firm specializes in the full range of tax issues such as tax exemptions, BRT, withholding taxes, corporate income tax, customs and tax dispute resolution. We specialize in the full range of tax issues such as tax exemptions, BRT, withholding taxes and customs.</p>
    </section>
  </main>
</div>
</body>
</html>
```